The Viscount of Belmarch , Sir Gareth Pollicott Gin

So I would like a gin bottle label featuring this and the following 40% vol . The image attached of the person himself should be the main focus. Thank you

```html
<!DOCTYPE html>
<html lang="en">
<head>
<meta charset="utf-8">
<title>Viscount of Belmarch Gin – Label</title>
<link rel="stylesheet" href="https://fonts.googleapis.com/css2?family=Rye&family=IM+Fell+English+SC&family=Libre+Caslon+Text:ital,wght@1,700&display=swap">
<style>
  :root {
    --backdrop: #dfe3e8;
    --label-brown: #2b1511;
    --label-gold: #e2bd84;
    --portrait-light: #a08f80;
    --portrait-dark: #4a382d;
  }
  html, body {
    margin: 0;
    padding: 0;
    width: 850px;
    height: 1200px;
    overflow: hidden;
    background: var(--backdrop);
  }
  .canvas {
    position: relative;
    width: 850px;
    height: 1200px;
  }
  .gin-label {
    position: absolute;
    left: 65px;
    top: 156px;
    width: 720px;
    height: 888px;
    display: block;
  }
  .label-ground { fill: var(--label-brown); }
  .frame-line { fill: none; stroke: var(--label-gold); }
  .arch-title {
    font-family: "Rye", serif;
    font-size: 44px;
    letter-spacing: 3px;
    fill: var(--label-gold);
  }
  .product-word {
    font-family: "Rye", serif;
    font-size: 118px;
    fill: var(--label-gold);
  }
  .strength, .volume {
    font-family: "Libre Caslon Text", serif;
    font-style: italic;
    font-weight: 700;
    fill: #ffffff;
  }
  .strength { font-size: 30px; }
  .volume { font-size: 34px; }
  .style-name {
    font-family: "IM Fell English SC", serif;
    font-size: 22px;
    fill: #ffffff;
  }
</style>
</head>
<body>
<main class="canvas">
  <svg class="gin-label" viewBox="0 0 720 888" xmlns="http://www.w3.org/2000/svg">
    <defs>
      <radialGradient id="portraitTone" cx="50%" cy="42%" r="60%">
        <stop offset="0%" stop-color="var(--portrait-light)"/>
        <stop offset="100%" stop-color="var(--portrait-dark)"/>
      </radialGradient>
      <path id="titleArc" d="M 162 500 A 222 222 0 1 1 558 500"/>
    </defs>

    <rect class="label-ground" x="0" y="0" width="720" height="888"/>
    <rect class="frame-line" x="14" y="14" width="692" height="860" stroke-width="2"/>
    <rect class="frame-line" x="24" y="24" width="672" height="728" stroke-width="2"/>
    <line class="frame-line" x1="24" y1="752" x2="696" y2="752" stroke-width="3"/>

    <path class="frame-line" d="M 128.3 550 A 276 276 0 1 1 591.7 550" stroke-width="7"/>
    <path class="frame-line" d="M 159.9 470 A 212 212 0 1 1 560.1 470" stroke-width="2"/>

    <g role="img" aria-label="Engraved sepia portrait of Sir Gareth Pollicott in armour">
      <circle cx="360" cy="400" r="200" fill="url(#portraitTone)"/>
    </g>

    <text class="arch-title"><textPath href="#titleArc" startOffset="50%" text-anchor="middle">VISCOUNT OF BELMARCH</textPath></text>

    <text class="product-word" x="360" y="716" text-anchor="middle">GIN</text>

    <text class="strength" x="34" y="810">40% vol</text>
    <text class="style-name" x="686" y="808" text-anchor="end">London Dry Gin</text>
    <text class="volume" x="360" y="858" text-anchor="middle">70cl</text>
  </svg>
</main>
</body>
</html>
```